Multiple Packaging Solutions for LED bulbs

We need a packaging design for led bulbs for our company. We need something that can be easily adjusted in different packaging types, as we have multiple different products. It needs to be fresh, friendly, happy but at the same time corporate. We provide some basic packaging dimensions and also our logo in the respective files. The packaging could be of plastic/trasparent, or carton (regular or ecofriendly)

It Company

```html
<!DOCTYPE html>
<html lang="en">
<head>
<meta charset="utf-8">
<title>brightnest – LED Panel Packaging</title>
<link rel="stylesheet" href="https://fonts.googleapis.com/css2?family=Titillium+Web:wght@300&family=Tinos&display=swap">
<style>
  :root {
    --backdrop: #c9c9c9;
    --carton-white: #ffffff;
    --carton-edge: #dcdcdc;
    --ink-grey: #3b3b3b;
    --bulb-grey: #4a4a4a;
    --accent-orange: #f08a00;
    --accent-amber: #f2a81d;
    --accent-coral: #e0603a;
    --accent-magenta: #c2185b;
    --panel-grey-light: #f4f4f4;
    --panel-grey-dark: #d2d2d2;
  }
  * { box-sizing: border-box; margin: 0; padding: 0; }
  html, body { width: 1200px; height: 960px; overflow: hidden; }
  body { background: var(--backdrop); font-family: "Titillium Web", sans-serif; }

  .dieline { position: relative; width: 1200px; height: 960px; }

  .panel {
    position: absolute;
    background: var(--carton-white);
    border: 1px solid var(--carton-edge);
    overflow: hidden;
  }
  .panel--top    { left: 120px; top: 80px;  width: 300px; height: 140px; }
  .panel--front  { left: 120px; top: 220px; width: 300px; height: 620px; }
  .panel--side-a { left: 420px; top: 220px; width: 180px; height: 620px; }
  .panel--back   { left: 600px; top: 220px; width: 300px; height: 620px;
                   background: linear-gradient(160deg, var(--panel-grey-dark) 0%, var(--panel-grey-light) 55%, var(--carton-white) 100%); }
  .panel--side-b { left: 900px; top: 220px; width: 180px; height: 620px; }

  /* Bulb artwork areas */
  .bulb-art { position: absolute; border-radius: 10px; }
  .bulb-art--top {
    right: 0; top: 0; width: 170px; height: 56px; border-radius: 0 0 0 10px;
    background: linear-gradient(90deg, var(--accent-amber), var(--accent-orange));
  }
  .bulb-art--front {
    left: 150px; top: 60px; width: 150px; height: 520px; border-radius: 150px 0 0 20px;
    background: linear-gradient(180deg, var(--bulb-grey) 0%, #6a6a6a 100%);
    opacity: .85;
  }
  .bulb-art--front-mark {
    left: 34px; top: 60px; width: 90px; height: 120px;
    background: linear-gradient(160deg, var(--accent-magenta), var(--accent-coral) 50%, var(--accent-amber));
    opacity: .8;
  }
  .bulb-art--side-a {
    left: 0; top: 20px; width: 80px; height: 540px; border-radius: 0 80px 10px 0;
    background: linear-gradient(180deg, var(--accent-coral) 0%, var(--accent-amber) 40%, var(--accent-magenta) 100%);
    opacity: .85;
  }
  .bulb-art--side-b {
    left: 0; top: 0; width: 80px; height: 320px; border-radius: 0 0 80px 0;
    background: linear-gradient(180deg, var(--accent-orange) 0%, var(--bulb-grey) 100%);
    opacity: .85;
  }
  .bulb-art--side-b-mark {
    left: 90px; top: 40px; width: 60px; height: 150px;
    background: linear-gradient(180deg, var(--accent-magenta), var(--accent-amber));
    opacity: .8;
  }

  .brand-lockup {
    position: absolute;
    display: flex;
    align-items: center;
    gap: 10px;
    color: var(--ink-grey);
    font-weight: 300;
    line-height: 1;
  }
  .brand-lockup__dot {
    width: 22px; height: 22px;
    border-radius: 50%;
    background: var(--accent-orange);
    flex: none;
  }
  .panel--top .brand-lockup   { left: 30px; top: 76px; font-size: 24px; }
  .panel--back .brand-lockup  { left: 30px; top: 36px; font-size: 30px; }

  .brand-vertical {
    position: absolute;
    writing-mode: vertical-rl;
    color: var(--ink-grey);
    font-weight: 300;
    line-height: 1;
    letter-spacing: 1px;
  }
  .panel--front .brand-vertical  { left: 50px; top: 230px; font-size: 72px; }
  .panel--side-a .brand-vertical { left: 118px; top: 330px; font-size: 26px; }
  .panel--side-b .brand-vertical { left: 118px; top: 330px; font-size: 26px; }
  .panel--back .brand-vertical   { right: 30px; top: 230px; font-size: 58px; }

  .spec-list {
    position: absolute;
    left: 28px; top: 230px;
    list-style: none;
    font-family: "Tinos", serif;
    font-size: 15px;
    line-height: 1.2;
    color: var(--ink-grey);
  }

  .cert-marks {
    position: absolute;
    left: 28px; bottom: 36px;
    display: flex;
    gap: 8px;
  }
  .cert-marks__item {
    width: 20px; height: 20px;
    background: var(--accent-magenta);
    border-radius: 50%;
  }
  .cert-marks__item--square { border-radius: 3px; }
</style>
</head>
<body>
  <main class="dieline">
    <section class="panel panel--top" aria-label="Top flap">
      <div class="bulb-art bulb-art--top" role="img" aria-label="Orange light bulb line artwork"></div>
      <div class="brand-lockup"><span class="brand-lockup__dot"></span>brightnest</div>
    </section>

    <section class="panel panel--front" aria-label="Front panel">
      <div class="bulb-art bulb-art--front-mark" role="img" aria-label="Pair of colourful light bulbs artwork"></div>
      <div class="bulb-art bulb-art--front" role="img" aria-label="Large grey light bulb outline artwork"></div>
      <div class="brand-vertical">brightnest</div>
    </section>

    <section class="panel panel--side-a" aria-label="Side panel">
      <div class="bulb-art bulb-art--side-a" role="img" aria-label="Orange and magenta light bulb outline artwork"></div>
      <div class="brand-vertical">brightnest</div>
    </section>

    <section class="panel panel--back" aria-label="Product information panel">
      <div class="brand-lockup"><span class="brand-lockup__dot"></span>brightnest</div>
      <ul class="spec-list">
        <li>BN-SQPN-3030W</li>
        <li>LED Panel</li>
        <li>Size: 296x296mm</li>
        <li>Wattage: 30W</li>
        <li>CCT: 3000K</li>
        <li>Voltage: 100-240VAC</li>
        <li>CRI&gt;80</li>
      </ul>
      <div class="brand-vertical">brightnest</div>
      <div class="cert-marks" aria-label="Certification marks">
        <span class="cert-marks__item cert-marks__item--square"></span>
        <span class="cert-marks__item"></span>
        <span class="cert-marks__item cert-marks__item--square"></span>
        <span class="cert-marks__item"></span>
      </div>
    </section>

    <section class="panel panel--side-b" aria-label="Side panel">
      <div class="bulb-art bulb-art--side-b" role="img" aria-label="Grey and orange light bulb outline artwork"></div>
      <div class="bulb-art bulb-art--side-b-mark" role="img" aria-label="Pair of colourful light bulbs artwork"></div>
      <div class="brand-vertical">brightnest</div>
    </section>
  </main>
</body>
</html>
```